Brochure Design

Looking for a sharp-looking brochure to provide to managers and customers. We have a ton of pictures, so please reach out if you need more! Or get some off google, haha.
www.ridgecrestpavingcrew.example

We provide these services below:

- Seal Coating
- Striping
- Crack Filling
- Paving
- Concrete
- Wheel blocks
- Sign installation
- 24 hour water break service
- Power Washing
- Commercial Curbing
- Bollard installation
- Thermoplastic
- Gas station pump area steam cleaning
- Street Sweeping
- Grading
- Material Delivery

This will be a 8" x 11" TRI FOLD BROCHURE. I will need to be able to upload it to quilla press.

```html
<!DOCTYPE html>
<html lang="en">
<head>
<meta charset="utf-8">
<title>Ridgecrest Paving Crew — Tri-fold Brochure</title>
<link href="https://fonts.googleapis.com/css2?family=Bebas+Neue&family=Montserrat:wght@400;500;600;700;800&display=swap" rel="stylesheet">
<style>
  :root {
    --asphalt: #1b1b1b;
    --asphalt-deep: #111111;
    --safety-yellow: #f2b51d;
    --paper: #f3f3f1;
    --ink: #222222;
    --white: #ffffff;
    --stage: #e9eaec;
    --muted: #cfcfcf;
    --sky: #8fb4dc;
    --foliage: #6f9a3c;
    --pavement: #55595e;
    --glass: #b9b2a6;
    --concrete: #b4b6b3;
  }
  * { box-sizing: border-box; margin: 0; padding: 0; }
  html, body { width: 1200px; height: 2399px; overflow: hidden; }
  body {
    background: var(--stage);
    font-family: "Montserrat", Arial, sans-serif;
    color: var(--ink);
    position: relative;
  }
  .spread {
    position: absolute;
    left: 60px;
    width: 1080px;
    height: 835px;
    display: grid;
    grid-template-columns: repeat(3, 1fr);
    box-shadow: 0 18px 40px rgba(0,0,0,.18);
    overflow: hidden;
  }
  .spread--outside { top: 305px; background: var(--asphalt); }
  .spread--inside { top: 1260px; background: var(--paper); }

  .panel { position: relative; height: 100%; overflow: hidden; }
  .spread--outside .panel + .panel { border-left: 1px solid #2c2c2c; }
  .spread--inside .panel + .panel { border-left: 1px solid #dddddd; }

  .footer-band {
    position: absolute; left: 0; right: 0; bottom: 0; height: 30px;
    background: var(--safety-yellow);
    border-top: 4px solid var(--asphalt-deep);
  }
  .spread--inside .footer-band { height: 16px; border-top-width: 3px; }

  .brand {
    display: flex; align-items: center; justify-content: center; gap: 12px;
    height: 150px;
  }
  .brand__dot { width: 22px; height: 22px; border-radius: 50%; background: var(--white); }
  .brand__name {
    font-weight: 800; font-size: 21px; line-height: 1.05; color: var(--white);
    text-transform: uppercase; letter-spacing: .5px;
  }

  .photo { display: block; width: 100%; }
  .rule { height: 3px; background: var(--safety-yellow); }

  .label {
    display: inline-block; background: var(--safety-yellow); color: var(--asphalt-deep);
    font-family: "Bebas Neue", Impact, sans-serif; font-size: 19px; letter-spacing: 1px;
    padding: 2px 8px 0;
  }
  .phone {
    font-family: "Bebas Neue", Impact, sans-serif; color: var(--white);
    font-size: 46px; line-height: 1; letter-spacing: 1px;
  }
  .web {
    display: inline-block; background: var(--safety-yellow); color: var(--asphalt-deep);
    font-size: 12px; font-weight: 700; padding: 4px 10px;
  }

  /* Outside: about panel */
  .about__photo { height: 250px; background: linear-gradient(180deg, var(--sky) 0 30%, var(--foliage) 30% 55%, var(--concrete) 55% 75%, var(--pavement) 75%); }
  .about__body { padding: 26px 32px 0; color: var(--muted); }
  .about__title {
    font-weight: 700; color: var(--safety-yellow);
    font-size: 17px; letter-spacing: 1px; margin-bottom: 14px;
  }
  .about__body p { font-size: 11px; line-height: 1.6; margin-bottom: 10px; }
  .about__contact { position: absolute; left: 32px; bottom: 58px; }

  /* Outside: back panel */
  .back__photo { height: 330px; background: linear-gradient(180deg, var(--glass) 0 45%, #2f4f9a 45% 62%, var(--pavement) 62%); }
  .back__contact { padding: 26px 30px 0; text-align: center; }
  .back__contact .phone { margin-top: 6px; }
  .office { margin-top: 12px; color: var(--white); font-size: 11px; line-height: 1.5; }
  .office strong { color: var(--safety-yellow); font-weight: 700; letter-spacing: .5px; display: block; }
  .back__web { margin-top: 16px; }

  /* Outside: cover panel */
  .cover__photo { height: 330px; background: linear-gradient(180deg, var(--glass) 0 50%, var(--pavement) 50%); }
  .cover__text { padding: 30px 26px 0; }
  .cover__kicker {
    font-family: "Bebas Neue", Impact, sans-serif; color: var(--safety-yellow);
    font-size: 15px; white-space: nowrap;
  }
  .cover__headline {
    font-family: "Bebas Neue", Impact, sans-serif; color: var(--white);
    font-size: 36px; line-height: 1; margin: 4px 0 12px; white-space: nowrap;
  }
  .cover__lede { color: var(--white); font-size: 13px; line-height: 1.55; font-weight: 500; }
  .cover__web { margin-top: 18px; }

  /* Inside */
  .services-band {
    position: absolute; left: 0; top: 0; width: 720px; height: 330px; z-index: 1;
  }
  .services-band__photos {
    position: absolute; left: 14px; top: 16px; right: 14px;
    display: grid; grid-template-columns: repeat(3, 1fr); gap: 10px; height: 205px;
  }
  .tile--lot { background: linear-gradient(180deg, #6f7f88 0 40%, #2b3338 40%); }
  .tile--wash { background: linear-gradient(180deg, #8a9a9c 0 35%, #4b5759 35%); }
  .tile--curb { background: linear-gradient(180deg, #6d9a3f 0 70%, #8a7a62 70%); }
  .services-title {
    position: absolute; left: 0; right: 0; top: 248px; text-align: center;
    font-family: "Bebas Neue", Impact, sans-serif; color: var(--white);
    font-size: 32px; letter-spacing: 1px;
  }
  .service-list {
    position: absolute; top: 360px; left: 40px; list-style: none;
  }
  .service-list li {
    display: flex; align-items: center; gap: 12px;
    font-size: 15px; font-weight: 500; color: var(--ink);
    height: 50px;
  }
  .service-icon { width: 28px; height: 28px; flex: none; }

  .gallery {
    position: absolute; left: 22px; right: 22px; top: 22px;
    display: grid; grid-template-columns: 1fr 1fr; grid-auto-rows: 92px; gap: 12px;
  }
  .g1 { background: linear-gradient(180deg, #7f9a6a 0 40%, #4a4f4a 40%); }
  .g2 { background: linear-gradient(180deg, #6e9ad3 0 60%, #3d4248 60%); }
  .g3 { background: linear-gradient(180deg, #2e4f8f 0 50%, #2b2f36 50%); }
  .g4 { background: linear-gradient(180deg, #8aa0b8 0 45%, #5f7150 45%); }
  .g5 { background: linear-gradient(180deg, #5a5c5c 0 55%, #c9a329 55%); }
  .g6 { background: linear-gradient(180deg, #9ea4a6 0 40%, #c4c6c2 40%); }
  .g7 { background: linear-gradient(180deg, #9bb0c5 0 40%, #7a4f3a 40%); }
  .g8 { background: linear-gradient(180deg, #a9b0b3 0 35%, #8a8f91 35%); }
  .g9 { background: linear-gradient(180deg, #8fa6bc 0 45%, #6f5a48 45%); }
  .g10 { background: linear-gradient(180deg, #c8c6c0 0 65%, #e2553a 65%); }
  .gallery__contact { position: absolute; right: 24px; bottom: 36px; text-align: right; }
  .gallery__contact .phone { color: var(--asphalt-deep); }
</style>
</head>
<body>

<section class="spread spread--outside" aria-label="Brochure outside">
  <article class="panel about">
    <div class="photo about__photo" role="img" aria-label="Photo of a freshly paved storage facility lot under a blue sky with trees"></div>
    <div class="rule"></div>
    <div class="about__body">
      <h2 class="about__title">ABOUT US</h2>
      <p>Ridgecrest Paving Crew is a full service parking lot maintenance and power washing company with over 10 years of providing outstanding service in the region. As a fully licensed and insured company, we are now taking our expertise into new areas.</p>
      <p>We believe that first impressions are everything. Your parking lot is the first thing customers see, and clean striping and a fresh seal make a strong statement about your business.</p>
      <p>We offer complete layout and line striping services using quality equipment and materials, and we work hard to complete every job promptly and on time.</p>
    </div>
    <div class="about__contact">
      <span class="label">GET IN TOUCH</span>
      <div class="phone">1-800-PAVECREW</div>
    </div>
    <div class="footer-band"></div>
  </article>

  <article class="panel back">
    <div class="brand">
      <span class="brand__dot"></span>
      <span class="brand__name">Ridgecrest<br>Paving Crew</span>
    </div>
    <div class="rule"></div>
    <div class="photo back__photo" role="img" aria-label="Photo of a line striping machine in front of a storefront with a freshly striped accessible parking space"></div>
    <div class="rule"></div>
    <div class="back__contact">
      <span class="label">GET IN TOUCH</span>
      <div class="phone">1-800-PAVECREW</div>
      <p class="office"><strong>IDAHO OFFICE:</strong>1400 N Cedar Road, Pine Falls, ID 83000</p>
      <p class="office"><strong>WASHINGTON OFFICE:</strong>5120 Lakeview Ave SE, Fern Valley, WA 98000</p>
      <div class="back__web"><span class="web">www.ridgecrestpavingcrew.example</span></div>
    </div>
    <div class="footer-band"></div>
  </article>

  <article class="panel cover">
    <div class="brand">
      <span class="brand__dot"></span>
      <span class="brand__name">Ridgecrest<br>Paving Crew</span>
    </div>
    <div class="rule"></div>
    <div class="photo cover__photo" role="img" aria-label="Photo of a storefront with freshly striped parking stalls and a blue accessible space"></div>
    <div class="rule"></div>
    <div class="cover__text">
      <p class="cover__kicker">PARKING LOT STRIPING &amp; SEALCOATING, CRACK FILLING</p>
      <h1 class="cover__headline">REPAIRS &amp; MAINTENANCE</h1>
      <p class="cover__lede">Ridgecrest Paving Crew is a leader in parking lot maintenance in northern Idaho &amp; eastern Washington.</p>
      <div class="cover__web"><span class="web">www.ridgecrestpavingcrew.example</span></div>
    </div>
    <div class="footer-band"></div>
  </article>
</section>

<section class="spread spread--inside" aria-label="Brochure inside">
  <svg class="services-band" viewBox="0 0 720 330" preserveAspectRatio="none" aria-hidden="true">
    <path d="M0 0H720V300C560 270 460 320 360 300C260 280 160 320 0 300Z" fill="#1b1b1b"/>
    <path d="M0 304C160 324 260 284 360 304C460 324 560 274 720 304" stroke="#f2b51d" stroke-width="3" fill="none"/>
  </svg>
  <div class="services-band">
    <div class="services-band__photos">
      <div class="tile--lot" role="img" aria-label="Photo of a sealcoated lot with fresh striping at dusk"></div>
      <div class="tile--wash" role="img" aria-label="Photo of power washing a concrete surface"></div>
      <div class="tile--curb" role="img" aria-label="Photo of new commercial curbing beside a green lawn"></div>
    </div>
    <h2 class="services-title">OUR PROVIDED SERVICES BELOW</h2>
  </div>

  <article class="panel">
    <ul class="service-list">
      <li><svg class="service-icon" viewBox="0 0 28 28"><circle cx="14" cy="14" r="14" fill="#1b1b1b"/><rect x="7" y="12" width="14" height="5" fill="#fff"/></svg>Seal Coating</li>
      <li><svg class="service-icon" viewBox="0 0 28 28"><circle cx="14" cy="14" r="14" fill="#1b1b1b"/><path d="M9 20L13 8M15 8L19 20" stroke="#fff" stroke-width="2"/></svg>Striping</li>
      <li><svg class="service-icon" viewBox="0 0 28 28"><circle cx="14" cy="14" r="14" fill="#1b1b1b"/><path d="M8 10L12 14L10 16L16 20" stroke="#fff" stroke-width="2" fill="none"/></svg>Crack Filling</li>
      <li><svg class="service-icon" viewBox="0 0 28 28"><circle cx="14" cy="14" r="14" fill="#1b1b1b"/><circle cx="14" cy="14" r="6" stroke="#fff" stroke-width="2" fill="none"/></svg>Paving</li>
      <li><svg class="service-icon" viewBox="0 0 28 28"><circle cx="14" cy="14" r="14" fill="#1b1b1b"/><rect x="8" y="10" width="12" height="8" rx="2" fill="#fff"/></svg>Concrete</li>
      <li><svg class="service-icon" viewBox="0 0 28 28"><circle cx="14" cy="14" r="14" fill="#1b1b1b"/><rect x="7" y="15" width="14" height="4" fill="#fff"/><circle cx="14" cy="11" r="3" fill="#fff"/></svg>Wheel blocks</li>
      <li><svg class="service-icon" viewBox="0 0 28 28"><circle cx="14" cy="14" r="14" fill="#1b1b1b"/><rect x="9" y="7" width="10" height="8" fill="#fff"/><rect x="13" y="15" width="2" height="6" fill="#fff"/></svg>Sign installation</li>
      <li><svg class="service-icon" viewBox="0 0 28 28"><circle cx="14" cy="14" r="14" fill="#1b1b1b"/><path d="M14 7C10 13 10 16 14 20C18 16 18 13 14 7Z" fill="#fff"/></svg>24 hour water break<br>service</li>
    </ul>
    <div class="footer-band"></div>
  </article>

  <article class="panel">
    <ul class="service-list">
      <li><svg class="service-icon" viewBox="0 0 28 28"><circle cx="14" cy="14" r="14" fill="#1b1b1b"/><path d="M8 18L18 8M11 20L20 11" stroke="#fff" stroke-width="2"/></svg>Power Washing</li>
      <li><svg class="service-icon" viewBox="0 0 28 28"><circle cx="14" cy="14" r="14" fill="#1b1b1b"/><path d="M7 18H21V14H12V10H7Z" fill="#fff"/></svg>Commercial Curbing</li>
      <li><svg class="service-icon" viewBox="0 0 28 28"><circle cx="14" cy="14" r="14" fill="#1b1b1b"/><rect x="11" y="7" width="6" height="14" rx="2" fill="#fff"/></svg>Bollard installation</li>
      <li><svg class="service-icon" viewBox="0 0 28 28"><circle cx="14" cy="14" r="14" fill="#1b1b1b"/><path d="M8 20L14 8L20 20Z" fill="#fff"/></svg>Thermoplastic</li>
      <li><svg class="service-icon" viewBox="0 0 28 28"><circle cx="14" cy="14" r="14" fill="#1b1b1b"/><rect x="9" y="8" width="8" height="12" fill="#fff"/><path d="M17 11H20V18" stroke="#fff" stroke-width="2" fill="none"/></svg>Gas station pump area<br>steam cleaning</li>
      <li><svg class="service-icon" viewBox="0 0 28 28"><circle cx="14" cy="14" r="14" fill="#1b1b1b"/><path d="M10 7L14 17M9 19H19" stroke="#fff" stroke-width="2"/></svg>Street Sweeping</li>
      <li><svg class="service-icon" viewBox="0 0 28 28"><circle cx="14" cy="14" r="14" fill="#1b1b1b"/><path d="M7 19H21L17 12H11Z" fill="#fff"/></svg>Grading</li>
      <li><svg class="service-icon" viewBox="0 0 28 28"><circle cx="14" cy="14" r="14" fill="#1b1b1b"/><rect x="7" y="11" width="9" height="7" fill="#fff"/><path d="M16 13H20L21 18H16Z" fill="#fff"/></svg>Material Delivery</li>
    </ul>
    <div class="footer-band"></div>
  </article>

  <article class="panel">
    <div class="gallery">
      <div class="g1" role="img" aria-label="Photo of a newly paved hillside road"></div>
      <div class="g2" role="img" aria-label="Photo of a large sealed commercial lot"></div>
      <div class="g3" role="img" aria-label="Photo of a striped lot at dusk"></div>
      <div class="g4" role="img" aria-label="Photo of a paved lot beside evergreen trees"></div>
      <div class="g5" role="img" aria-label="Photo of paving equipment at work"></div>
      <div class="g6" role="img" aria-label="Photo of fresh concrete curbing"></div>
      <div class="g7" role="img" aria-label="Photo of a sealed lot in front of a restaurant"></div>
      <div class="g8" role="img" aria-label="Photo of a newly poured concrete pad"></div>
      <div class="g9" role="img" aria-label="Photo of a striped lot in front of a building"></div>
      <div class="g10" role="img" aria-label="Photo of a work zone marked with traffic cones"></div>
    </div>
    <div class="gallery__contact">
      <span class="label">GET IN TOUCH</span>
      <div class="phone">1-800-PAVECREW</div>
    </div>
    <div class="footer-band"></div>
  </article>
</section>

</body>
</html>
```